Bright Harbor; Teaching Series Art.

Our church is going to be teaching a series of messages under the topic/title: Bright Harbor. Just looking for a simple design to help with this. I have uploaded a design that is an example of what we were thinking.

The point of the design is to communicate a new way of doing things (given some of the impact of the coronavirus) - although the background doesn't need to be too busy - just something simple, clean and modern.

Even though it's for a church, we don't need any religious art in the background (crosses, people praying, etc.) Looking for a similar feel background to the one we uploaded.

The only text should be Bright Harbor and maybe highlighting the word Bright somehow.

Font styles to use
Sans Serif

Requirements
Must have
• Title of "Bright Harbor" - no other text.

```html
<!DOCTYPE html>
<html lang="en">
<head>
<meta charset="utf-8">
<title>Bright Harbor — Teaching Series</title>
<link href="https://fonts.googleapis.com/css2?family=Fira+Sans:wght@700&display=swap" rel="stylesheet">
<style>
  :root {
    --navy-deep: #1b1f44;
    --navy: #212858;
    --navy-glow: #2a3578;
    --mint: #4ee59b;
    --white: #ffffff;
  }
  html, body {
    margin: 0;
    padding: 0;
    width: 1200px;
    height: 675px;
    overflow: hidden;
    background: var(--navy-deep);
  }
  .series-art {
    position: relative;
    width: 1200px;
    height: 675px;
    overflow: hidden;
  }
  .backdrop {
    position: absolute;
    inset: 0;
    background:
      radial-gradient(ellipse 70% 35% at 30% 28%, rgba(42, 53, 120, 0.55), transparent 70%),
      radial-gradient(ellipse 60% 30% at 75% 75%, rgba(42, 53, 120, 0.55), transparent 70%),
      linear-gradient(180deg, var(--navy-deep) 0%, var(--navy) 50%, var(--navy-deep) 100%);
  }
  .title-frame {
    position: absolute;
    inset: 0;
  }
  .title {
    position: absolute;
    left: 0;
    right: 0;
    top: 308px;
    margin: 0;
    text-align: center;
    font-family: "Fira Sans", sans-serif;
    font-weight: 700;
    font-size: 64px;
    line-height: 1;
    color: var(--mint);
    white-space: nowrap;
  }
  .title .highlight {
    text-shadow: -2px -2px 0 var(--white);
  }
</style>
</head>
<body>
  <main class="series-art">
    <div class="backdrop" role="img" aria-label="Flowing blue digital wave mesh with dotted particle lines on deep navy"></div>

    <svg class="title-frame" width="1200" height="675" viewBox="0 0 1200 675" aria-hidden="true">
      <rect x="330" y="268" width="550" height="149" fill="none" stroke="var(--mint)" stroke-width="2.4"/>
      <rect x="322" y="257.5" width="550" height="150" fill="none" stroke="var(--white)" stroke-width="2.6"/>
    </svg>

    <h1 class="title"><span class="highlight">BRIGHT</span> Harbor</h1>
  </main>
</body>
</html>
```